Sidewalk Sign For Laundry Service

I'd like to make a sign that offers *free* laundry service for the next customers that bring in their laundry. There needs to be some immediacy in the design. The idea is to put out this sign when we are idle in the laundry and want to use the time to attract new customers. So somehow we need to communicate that the offer is for right now and will likely be gone in an hour or two. Attached are photos of the sign holder in place to give a feel for the location and environment. Obviously I'm looking for a much better design that the one currently in use.

Requirements:
* 23.25" x 35.5" - the full width will be visible but the top and bottom 0.5" will be hidden by the sign holder. It will be printed on coroplast.
* Must include a large arrow to show where the service is offered. We're off the main street so the arrow helps a lot. See the attached pictures of the sign being replaced.
* Needs to be visible to cars as they drive by.
* For the final product I'll need three versions. One with an arrow pointing to the right, one with an arrow pointing to the left, and one to go in the store window with no arrow.

Background on the service: We sort, wash, dry, and fold the laundry for customers and then neatly put it in a nice laundry bag that makes returning very convenient. Their laundry comes out fresh, clean, smelling great, and without the hassle of doing it themselves. We have a great return rate. Most customers that try out the service become long term customers.

Attached are two pictures of the sign holder with our current "Laundry Wash & Fold" sign. Also, our logo which would be nice to include to help with branding.

```html
<!DOCTYPE html>
<html lang="en">
<head>
<meta charset="utf-8">
<title>Free Laundry Wash &amp; Fold Today – Sidewalk Sign</title>
<link href="https://fonts.googleapis.com/css2?family=Passion+One:wght@400;700&display=swap" rel="stylesheet">
<style>
  :root {
    --brand-blue: #22409a;
    --brand-orange: #f26522;
    --panel-grey: #f2f2f4;
    --arrow-edge: #ffffff;
  }
  * { margin: 0; padding: 0; box-sizing: border-box; }
  html, body { width: 786px; height: 1200px; overflow: hidden; background: var(--brand-blue); }
  .sign {
    position: relative;
    width: 786px;
    height: 1200px;
    background: var(--brand-blue);
    font-family: "Passion One", "Arial Black", sans-serif;
  }
  .sign-panel {
    position: absolute;
    left: 26px; top: 26px;
    width: 732px; height: 1147px;
    background: var(--panel-grey);
    border: 2px solid var(--brand-orange);
  }
  .brand {
    position: absolute;
    left: 62px; top: 74px;
    display: flex;
    align-items: center;
    gap: 28px;
  }
  .brand-square {
    width: 150px; height: 150px;
    background: var(--brand-blue);
    border-radius: 6px;
  }
  .brand-name {
    font-weight: 400;
    font-size: 92px;
    line-height: 0.95;
    color: var(--brand-blue);
  }
  .headline {
    position: absolute;
    left: 0; width: 100%;
    text-align: center;
    line-height: 1;
    font-weight: 700;
    -webkit-text-stroke: 3px var(--brand-orange);
    paint-order: stroke fill;
  }
  .headline--free  { top: 318px; font-size: 150px; color: var(--brand-blue); letter-spacing: 2px; }
  .headline--laundry { top: 462px; font-size: 160px; color: var(--brand-orange); -webkit-text-stroke: 0; letter-spacing: 2px; }
  .headline--service { top: 622px; font-size: 122px; color: var(--brand-orange); -webkit-text-stroke: 0; }
  .headline--today { top: 762px; font-size: 200px; color: var(--brand-blue); letter-spacing: 3px; }
  .flourish {
    position: absolute;
    top: 374px;
    width: 138px; height: 36px;
    border-radius: 18px;
    background: linear-gradient(90deg, var(--brand-blue), #3a5ab8);
  }
  .flourish--left { left: 60px; }
  .flourish--right { right: 60px; }
  .direction-arrows {
    position: absolute;
    left: 0; top: 0;
    width: 786px; height: 1200px;
  }
</style>
</head>
<body>
  <main class="sign">
    <div class="sign-panel"></div>

    <header class="brand">
      <div class="brand-square"></div>
      <div class="brand-name">Fresh Fold<br>Laundry</div>
    </header>

    <div class="flourish flourish--left" role="img" aria-label="Decorative swirl ornament"></div>
    <div class="flourish flourish--right" role="img" aria-label="Decorative swirl ornament"></div>

    <h1 class="headline headline--free">FREE</h1>
    <p class="headline headline--laundry">LAUNDRY</p>
    <p class="headline headline--service">WASH &amp; FOLD</p>
    <p class="headline headline--today">TODAY</p>

    <svg class="direction-arrows" viewBox="0 0 786 1200" aria-label="Arrows pointing right">
      <g fill="var(--brand-orange)" stroke="var(--brand-blue)" stroke-width="4" stroke-linejoin="miter">
        <polygon points="42,992 200,992 262,1070 200,1150 42,1150 104,1070"/>
        <polygon points="224,992 386,992 448,1070 386,1150 224,1150 286,1070"/>
        <polygon points="438,992 680,992 746,1070 680,1150 438,1150 500,1070"/>
      </g>
      <g fill="none" stroke="var(--arrow-edge)" stroke-width="2">
        <polygon points="50,998 197,998 254,1070 197,1144 50,1144 110,1070"/>
        <polygon points="232,998 383,998 440,1070 383,1144 232,1144 292,1070"/>
        <polygon points="446,998 677,998 738,1070 677,1144 446,1144 506,1070"/>
      </g>
    </svg>
  </main>
</body>
</html>
```